Brindle Grass Services website design

We want to create a Sports turf website for our business Brindle Grass Services - we do sports turf management on sports fields around the Mackay region soccer rugby league softball fields etc from full turf management plans and maintenance to just supply and apply of turf management products and just supply of products with program we also do grounds facility maintenance at council facility's and grounds that require a higher level of care - we will up load our logos and fonts etc to assist with the colour pallet for the website - we will have to have a landing page a shop page with tabs a gallery tab along with a grants initiative and our coastals finest green tab also - our font for the txt is called ethnocentric
Updates

how do we open time for people to submit we have no one submitted

Industry/Entity Type

Turf

Coding

Coded - Design and coding required

Number of Pages Required

5+ page

Font styles to use
Other font styles liked:
• ethnocentric

Requirements
Must have
• I have mentioned some waffle in the description that should assist
Should not have
• anything not related

```html
<!DOCTYPE html>
<html lang="en">
<head>
<meta charset="utf-8">
<title>Brindle Grass Services</title>
<link href="https://fonts.googleapis.com/css2?family=Archivo:wdth,wght@62..125,400..900&family=Montserrat:wght@400;500;700&family=Domine:wght@400;500&family=Open+Sans:wght@400&display=swap" rel="stylesheet">
<style>
:root{
  --bg:#000;
  --lime:#9cff00;
  --white:#fff;
  --muted:#e6e6e6;
  --border:#4f9a12;
  --pill:#2a2a2a;
  --grass-dark:#1f4a0c;
  --grass:#3c9a18;
  --grass-bright:#4cc21d;
  --court:#1247d6;
}
*{margin:0;padding:0;box-sizing:border-box}
html,body{width:1200px;height:2474px;overflow:hidden;background:var(--bg);color:var(--white)}
body{position:relative;font-family:'Montserrat',sans-serif}
.display{font-family:'Archivo',sans-serif;font-stretch:125%;font-weight:800;text-transform:uppercase;letter-spacing:-0.5px}
.abs{position:absolute}

/* nav */
.brand{left:150px;top:44px;font-family:'Archivo',sans-serif;font-stretch:125%;font-weight:800;font-size:15px;line-height:30px;color:var(--white);display:flex;align-items:center;gap:8px}
.brand-mark{width:12px;height:12px;background:var(--lime)}
.nav{left:440px;top:46px;display:flex;align-items:center;gap:4px;font-family:'Domine',serif;font-size:13px}
.nav a{color:var(--white);text-decoration:none;padding:5px 10px;border-radius:4px}
.nav a.active{background:var(--pill)}
.nav svg{margin-left:8px}

/* hero */
.hero-title{left:152px;top:146px;width:430px;font-size:30px;line-height:33px}
.hero-copy{left:152px;top:254px;width:420px;font-size:12.4px;line-height:16.3px;color:var(--muted)}
.hero-copy p+p{margin-top:16px}
.hero-photo{left:586px;top:143px;width:461px;height:255px;border:2px solid var(--white);border-radius:6px;background:linear-gradient(160deg,#35b51a,#1f9a10 60%,#2aa814)}

/* choose */
.section-title{left:0;width:1200px;text-align:center}
.choose-title{top:466px;font-size:39px;line-height:44px}
.choose-title span{color:var(--lime);display:block}
.choose-sub{top:562px;left:230px;width:740px;text-align:center;font-size:12.6px;line-height:18px;color:var(--muted)}

.card{width:289px;height:339px;border:1px solid var(--border);border-radius:5px;overflow:hidden;background:#000}
.card-photo{height:200px;width:100%}
.card h3{font-size:14.5px;margin:14px 0 0 6px}
.stars{color:var(--lime);font-size:12px;letter-spacing:1px;margin:10px 0 0 7px}
.card p{font-size:9.6px;line-height:12.5px;color:var(--muted);margin:6px 6px 0}
.card p b{color:var(--lime)}
.plus{position:absolute;right:2px;bottom:2px;width:20px;height:19px;background:var(--lime);color:#000;font-size:12px;text-align:center;line-height:19px;border-radius:2px}

.promo{left:455px;top:1005px;width:290px;height:340px;background:var(--lime);border-radius:4px;color:#000;overflow:hidden}
.promo .vt{position:absolute;font-family:'Archivo',sans-serif;font-stretch:125%;font-weight:800;font-size:17px;white-space:nowrap}
.promo .left{left:30px;top:14px;writing-mode:vertical-rl}
.promo .right{right:30px;top:14px;writing-mode:vertical-rl;transform:rotate(180deg)}
.promo .top{left:60px;top:10px;transform:rotate(180deg)}
.promo .bottom{left:40px;top:254px}
.promo-photo{position:absolute;left:90px;top:44px;width:110px;height:210px;background:linear-gradient(180deg,#ece6d6,#cfc7b4);border-radius:40px 40px 10px 10px}
.shop-btn{position:absolute;left:78px;top:290px;width:135px;height:38px;background:#000;color:var(--white);border-radius:6px;font-family:'Archivo',sans-serif;font-stretch:110%;font-weight:800;font-size:12.5px;text-align:center;line-height:38px}

.lawn-feature{left:454px;top:1384px;width:593px;height:338px;border-radius:5px;overflow:hidden;background:radial-gradient(circle at 78% 12%,#f3c455 0,#8a6a26 14%,transparent 34%),linear-gradient(180deg,#2b2a1c 0%,#1b2a10 45%,#3d7a18 75%,#254d0e 100%)}
.lawn-feature .ghost{position:absolute;left:0;width:100%;bottom:-10px;text-align:center;font-size:38px;color:rgba(255,255,255,.28)}

.view-more{left:531px;top:1755px;width:138px;height:36px;background:var(--lime);color:#000;border-radius:4px;font-size:12.5px;text-align:center;line-height:36px}

/* newsletter */
.news-title{top:1856px;font-size:39px;line-height:46px}
.news-sub{top:1907px;font-size:12.6px;color:var(--muted)}
.subscribe{left:357px;top:1955px;width:485px;height:47px;border:1px solid #bbb;border-radius:5px}
.subscribe .btn{position:absolute;right:2px;top:2px;width:151px;height:41px;background:var(--lime);color:#000;border-radius:3px;font-size:12px;text-align:center;line-height:41px}
.socials{left:509px;top:2021px;display:flex;gap:12px}
.socials span{width:36px;height:36px;border-radius:50%;background:var(--lime)}

/* footer */
.foot-brand{left:150px;top:2128px;font-family:'Archivo',sans-serif;font-stretch:125%;font-weight:800;font-size:19px;display:flex;align-items:center;gap:10px}
.foot-brand i{width:14px;height:14px;background:var(--lime);display:block}
.foot-about{left:150px;top:2196px;width:240px;font-size:13px;line-height:17.5px;color:var(--muted)}
.foot-links{left:719px;top:2194px;list-style:none;font-family:'Domine',serif;font-size:13px;line-height:25px}
.contact{left:883px;top:2194px;font-family:'Domine',serif;font-size:13px;line-height:15px}
.contact li{list-style:none;display:flex;gap:12px;margin-bottom:13px}
.contact svg{flex:none}
.giant{left:152px;top:2336px;width:896px;text-align:center;font-size:49px;line-height:56px;background:linear-gradient(180deg,#3a3a3a 0%,#1a1a1a 60%,#000 100%);-webkit-background-clip:text;background-clip:text;color:transparent;white-space:nowrap}
.rule{left:0;top:2425px;width:1200px;height:1px;background:#555}
.copyright{top:2441px;font-family:'Open Sans',sans-serif;font-size:12.5px;color:var(--muted)}
</style>
</head>
<body>

<div class="abs brand"><span class="brand-mark"></span>Brindle Grass Services</div>
<nav class="abs nav">
  <a class="active">Home</a><a>About Us</a><a>Shop</a><a>Gallery Tab</a><a>Coastals Finest Green</a><a>Grants Initiative</a>
  <svg width="12" height="16" viewBox="0 0 12 16"><circle cx="6" cy="4" r="3.5" fill="#9cff00"/><path d="M0 16a6 6 0 0 1 12 0z" fill="#9cff00"/></svg>
</nav>

<h1 class="abs display hero-title">Step into excellence with world class turf built for champions.</h1>
<div class="abs hero-copy">
  <p>Lorem Ipsum Dolor Sit Amet, Consectetur Adipiscing Elit, Sed Do Eiusmod Tempor Incididunt Ut Labore Et Dolore Magna Aliqua. Ut Enim Ad Minim Veniam, Quis Nostrud Exercitation Ullamco Laboris Nisi Ut Aliquip Ex Ea Commodo Consequat.</p>
  <p>Lorem Ipsum Dolor Sit Amet, Consectetur Adipiscing Elit, Sed Do Eiusmod Tempor Incididunt Ut Labore Et Dolore Magna Aliqua. Ut Enim Ad Minim Veniam, Quis Nostrud Exercitation Ullamco Laboris Nisi Ut Aliquip Ex Ea Commodo Consequat.</p>
</div>
<div class="abs hero-photo" role="img" aria-label="Close view of a green sports pitch with white line markings and a ball"></div>

<h2 class="abs section-title display choose-title">Choose your<span>turf</span></h2>
<p class="abs choose-sub">There Are Many Variations Of Passages Of Lorem Ipsum Available, But The Majority Have Suffered Alteration In Some Form, By Injected Hum Our, Or Rando Mised Words Which Don't Look Even Slightly Believable.</p>

<article class="abs card" style="left:152px;top:628px">
  <div class="card-photo" role="img" aria-label="Golf green with a cup hole in dewy grass" style="background:radial-gradient(ellipse at 45% 40%,#6a9a3a,#2e5a14 50%,#132a06)"></div>
  <h3 class="display">Golf Turf</h3><div class="stars">★★★★★</div>
  <p>There Are Many Variations Of Passages Of Lorem Ipsum Available, But The Majority Have Suffered Alteration In Some Form, By Injected Hum Our, Or Rando Mised Words Which Don't <b>Read More.</b></p>
  <span class="plus">+</span>
</article>
<article class="abs card" style="left:455px;top:628px">
  <div class="card-photo" role="img" aria-label="Landscaped lawn in front of a house with palm trees" style="background:linear-gradient(180deg,#5a8fd0 0%,#7aa7d8 25%,#3e6a2a 50%,#3ca11a 75%,#2a8010)"></div>
  <h3 class="display">Landscaping Artificial Grass</h3><div class="stars">★★★★★</div>
  <p>There Are Many Variations Of Passages Of Lorem Ipsum Available, But The Majority Have Suffered Alteration In Some Form, By Injected Hum Our, Or Rando Mised Words Which Don't <b>Read More.</b></p>
  <span class="plus">+</span>
</article>
<article class="abs card" style="left:758px;top:628px">
  <div class="card-photo" role="img" aria-label="Striped cricket field under a clear sky" style="background:linear-gradient(180deg,#4f7fb0 0%,#3a7a40 12%,#57c62a 35%,#3fa81c 70%,#48b820)"></div>
  <h3 class="display">Cricket Turf</h3><div class="stars">★★★★★</div>
  <p>There Are Many Variations Of Passages Of Lorem Ipsum Available, But The Majority Have Suffered Alteration In Some Form, By Injected Hum Our, Or Rando Mised Words Which Don't <b>Read More.</b></p>
  <span class="plus">+</span>
</article>

<article class="abs card" style="left:152px;top:1005px">
  <div class="card-photo" role="img" aria-label="Top-down close view of artificial football grass" style="background:linear-gradient(135deg,#3f8a1a,#2d6e10 50%,#3a8418)"></div>
  <h3 class="display">Football Turf</h3><div class="stars">★★★★★</div>
  <p>There Are Many Variations Of Passages Of Lorem Ipsum Available, But The Majority Have Suffered Alteration In Some Form, By Injected Hum Our, Or Rando Mised Words Which Don't <b>Read More.</b></p>
  <span class="plus">+</span>
</article>

<div class="abs promo">
  <span class="vt top">WEATHER TURF.</span>
  <span class="vt left">PLAY ANYTIME ON ALL</span>
  <span class="vt right">PLAY ANYTIME ON ALL</span>
  <div class="promo-photo" role="img" aria-label="Cricket batsman in whites ready to play a shot"></div>
  <span class="vt bottom">WEATHER TURF. →</span>
  <div class="shop-btn">SHOP NOW</div>
</div>

<article class="abs card" style="left:759px;top:1005px">
  <div class="card-photo" role="img" aria-label="Low angle view of a dense natural lawn" style="background:linear-gradient(180deg,#4d6a30 0%,#5c8a2a 40%,#3b7a14 100%)"></div>
  <h3 class="display">Desert Blend Turf</h3><div class="stars">★★★★★</div>
  <p>There Are Many Variations Of Passages Of Lorem Ipsum Available, But The Majority Have Suffered Alteration In Some Form, By Injected Hum Our, Or Rando Mised Words Which Don't <b>Read More.</b></p>
  <span class="plus">+</span>
</article>

<article class="abs card" style="left:152px;top:1384px">
  <div class="card-photo" role="img" aria-label="Blue padel court surface with white lines" style="background:linear-gradient(160deg,#0e3fc8,#1a55e6 60%,#0f45d2)"></div>
  <h3 class="display">Padel Turf</h3><div class="stars">★★★★★</div>
  <p>There Are Many Variations Of Passages Of Lorem Ipsum Available, But The Majority Have Suffered Alteration In Some Form, By Injected Hum Our, Or Rando Mised Words Which Don't <b>Read More.</b></p>
  <span class="plus">+</span>
</article>

<div class="abs lawn-feature" role="img" aria-label="Robotic mower on a lush lawn at sunset">
  <span class="ghost display">Coastals Finest Green</span>
</div>

<div class="abs view-more display">View More</div>

<h2 class="abs section-title display news-title">Sign up for our newslatter</h2>
<p class="abs section-title news-sub">There Are Many Variations Of Passages Of Lorem Ipsum Available, But The Majority Have Believable.</p>
<div class="abs subscribe"><span class="btn display">Subscribe Now</span></div>
<div class="abs socials" aria-label="Social links"><span></span><span></span><span></span><span></span></div>

<div class="abs foot-brand"><i></i>Brindle Grass Services</div>
<p class="abs foot-about">It Is A Long Established Fact That A Reader Will Be Distracted By The Readable Content Of A Page When Looking At Its Layout.</p>
<ul class="abs foot-links">
  <li>About Us</li><li>Shop</li><li>Gallery Tab</li><li>Coastals Finest Green</li><li>Grants Initiative</li>
</ul>
<ul class="abs contact">
  <li><svg width="13" height="17" viewBox="0 0 13 17"><path d="M6.5 0A6.5 6.5 0 0 0 0 6.5C0 11 6.5 17 6.5 17S13 11 13 6.5A6.5 6.5 0 0 0 6.5 0z" fill="#9cff00"/><circle cx="6.5" cy="6.5" r="2.4" fill="#000"/></svg><span>42 Harbour Rd, Mackay,<br>QLD</span></li>
  <li><svg width="16" height="12" viewBox="0 0 16 12"><rect width="16" height="12" rx="1" fill="#9cff00"/><path d="M1 1l7 6 7-6" stroke="#000" stroke-width="1.4" fill="none"/></svg><span>info@brindlegrass.com</span></li>
  <li><svg width="15" height="15" viewBox="0 0 15 15"><path d="M3 0l3 3.5-1.6 2a9 9 0 0 0 5 5l2-1.6L15 12l-2 3C6 15 0 9 0 2z" fill="#9cff00"/></svg><span>(+61) 555 0142</span></li>
</ul>

<div class="abs giant display">Brindle Grass Services</div>
<div class="abs rule"></div>
<p class="abs section-title copyright">Copyright 2025 Northfield Studio All Rights Reserved</p>

</body>
</html>
```